I need a new business card for my hair salon based in Alder Bay, NT called "Lune's Salon". I have been in business at the same location for the past 15 years, and have recently remodeled the place to be a little bit more upscale and modern. Previously, my clientele's were mostly men, but now I would like to attract more female clientele into my business. I would like the design to attract the female's attention with it's modern touch, flowery, freshness with just enough information and not too compact. Simple, clean and professional is the look.
Requirements
Must Have:
- The design should include:
Business name: Lune's Salon
Hairstylist/Owner Name: Lune Okafor
Phone Number: (555) 418-6037
Website: www.lunehairstudio.example
Address: 48390 Harlow Penn Circle
Alder Bay, NT 20517
FRONT CARD should include:
- Logo (Business name)
- Slogan (Soft curls, bright days)
BACK CARD should include:
- Logo (Business name)
- Hairstyle name
- Phone number
- Website
- Address
Reason: There were some good submission for this project, but most of the submission were poorly designed, and did not have what I want. There isn't enough designs for me to choose from and not one of it stood out to me. I would like to extend it a bit longer to see if any other designer would step up to the plate, and deliver. Thank you.
Requirements
Must have
- The front side of the business card should only have the business name (Lune's Salon) and slogan, (Soft curls bright days) with a creative design.
The back side of the business card should have all the business information, and creative design that matches with the front, but not identical.
The first letter (V) in (Lune's) should have a flower design connected to it, which blends into the background design.
Nice to have
- Light color scheme.
Should not have
- The front, and back should not have the same design.
Do not include illustrations of a pair of scissors, combs or any objects in the design.
The design should not take the main focus from the business name and business information. It should blend well together... if that's possible.

```html
<!DOCTYPE html>
<html lang="en">
<head>
<meta charset="utf-8">
<title>Lune's Salon – Business Cards</title>
<link rel="stylesheet" href="https://fonts.googleapis.com/css2?family=Arimo:wght@400;700&family=Great+Vibes&display=swap">
<style>
  :root {
    --canvas: #ececec;
    --card-white: #ffffff;
    --ink: #1e1e1e;
    --ink-soft: #3a3a3a;
    --violet: #a24fd0;
    --violet-deep: #8a3bbd;
    --violet-light: #b466dc;
    --leaf: #5f9a2a;
    --on-violet: #ffffff;
  }
  * { box-sizing: border-box; margin: 0; padding: 0; }
  html, body { width: 1200px; height: 1000px; overflow: hidden; }
  body {
    background: var(--canvas);
    font-family: "Arimo", Arial, sans-serif;
    position: relative;
  }
  .card {
    position: absolute;
    width: 760px;
    height: 434px;
    border-radius: 4px;
    box-shadow: 0 8px 24px rgba(0,0,0,.18);
    overflow: hidden;
  }

  /* Contact side */
  .card--details { left: 120px; top: 50px; background: var(--card-white); }
  .card__flourish {
    position: absolute; right: 0; top: 0; width: 430px; height: 300px;
    background: radial-gradient(ellipse at 65% 35%, #e6e6e6 0%, #f1f1f1 45%, rgba(255,255,255,0) 75%);
  }
  .brand { position: absolute; display: flex; align-items: flex-end; gap: 8px; }
  .card--details .brand { left: 60px; top: 90px; }
  .brand__flower {
    width: 96px; height: 78px; border-radius: 40% 40% 10% 40%;
    background: linear-gradient(160deg, #b577e0 0%, #c99be6 45%, #9cc46a 100%);
    opacity: .85;
  }
  .brand__name {
    font-family: "Arimo", Arial, sans-serif;
    font-weight: 700;
    font-size: 48px;
    color: var(--violet);
    line-height: 1;
  }
  .tagline {
    font-family: "Great Vibes", cursive;
    font-size: 32px; color: var(--ink);
    position: absolute; line-height: 1.1;
  }
  .card--details .tagline { left: 168px; top: 176px; }
  .owner {
    position: absolute; left: 168px; top: 232px;
    font-family: "Great Vibes", cursive;
    font-size: 44px; line-height: 1.1; color: var(--leaf);
  }
  .contact { position: absolute; left: 168px; top: 300px; list-style: none; font-size: 18px; color: var(--ink-soft); }
  .contact li { display: flex; align-items: flex-start; gap: 12px; line-height: 24px; margin-bottom: 4px; }
  .contact svg { flex: 0 0 16px; margin-top: 4px; }
  .contact__web { font-weight: 700; color: var(--ink); }

  /* Brand side */
  .card--brand {
    left: 320px; top: 516px;
    background:
      repeating-linear-gradient(180deg, rgba(255,255,255,.035) 0 22px, rgba(0,0,0,.02) 22px 44px),
      linear-gradient(135deg, var(--violet-light), var(--violet-deep));
  }
  .card--brand .brand { left: 190px; top: 120px; }
  .card--brand .brand__flower {
    background: linear-gradient(160deg, #d8b4f0 0%, #c08ee6 50%, #9cc46a 100%);
    opacity: .7; width: 84px; height: 70px;
  }
  .card--brand .brand__name { color: var(--on-violet); font-size: 56px; }
  .card--brand .tagline { color: var(--on-violet); left: 290px; top: 196px; font-size: 34px; }
  .card--brand .web {
    position: absolute; left: 0; right: 0; bottom: 60px; text-align: center;
    font-weight: 700; font-size: 17px; color: var(--on-violet); letter-spacing: .3px;
  }
</style>
</head>
<body>

  <section class="card card--details" aria-label="Business card, contact side">
    <div class="card__flourish" role="img" aria-label="Faint grey floral swirl ornament"></div>
    <div class="brand">
      <div class="brand__flower" role="img" aria-label="Purple flower with green stem joined to the first letter"></div>
      <span class="brand__name">Lune's Salon</span>
    </div>
    <p class="tagline">Soft curls bright days</p>
    <p class="owner">Lune Okafor</p>
    <ul class="contact">
      <li>
        <svg width="16" height="16" viewBox="0 0 16 16" aria-hidden="true"><rect x="4" y="1" width="8" height="14" rx="2" fill="var(--leaf)"/><rect x="5.5" y="3" width="5" height="8" fill="#fff"/></svg>
        <span>(555) 418-6037</span>
      </li>
      <li>
        <svg width="16" height="16" viewBox="0 0 16 16" aria-hidden="true"><path d="M8 1a5 5 0 0 0-5 5c0 4 5 9 5 9s5-5 5-9a5 5 0 0 0-5-5z" fill="var(--leaf)"/><circle cx="8" cy="6" r="2" fill="#fff"/></svg>
        <span>48390 Harlow Penn Circle<br>Alder Bay, NT 20517</span>
      </li>
      <li>
        <svg width="16" height="16" viewBox="0 0 16 16" aria-hidden="true"><circle cx="8" cy="8" r="7" fill="var(--leaf)"/><path d="M1 8h14M8 1c3 3 3 11 0 14M8 1c-3 3-3 11 0 14" stroke="#fff" stroke-width="1" fill="none"/></svg>
        <span class="contact__web">www.lunehairstudio.example</span>
      </li>
    </ul>
  </section>

  <section class="card card--brand" aria-label="Business card, brand side">
    <div class="brand">
      <div class="brand__flower" role="img" aria-label="Light flower with green stem joined to the first letter"></div>
      <span class="brand__name">Lune's Salon</span>
    </div>
    <p class="tagline">Soft curls bright days</p>
    <p class="web">www.lunehairstudio.example</p>
  </section>

</body>
</html>
```